Webdesign für Realisation von  Bannern für unterschiedliche Werbenetzwerke
Webdesign für Realisation von Bannern für unterschiedliche Werbenetzwerke
Zielgruppe
Wir bieten Planung und Realistion von HTML5 Bannern für unterschiedliche Werbenetzwerke (besonders Velmora Adpilot) an.
Zielgruppe sind Unternehmen, welche einfach und kostengünstig online Banner erstellt haben möchten.
Aufgabenstellung
Die Webseite soll ein Onepager werden.
Die Webseite soll dem beigefügten Logo angepasst werden.
Bestellung und Bestätigung soll als eine Art Layover dargestellt werden.
Die Seite soll folgendes beinhalten:
- Header mit Logo, Telefon/Kontakt/Bestellbutton
- Intro
- Information zu Banner und Zielgruppenausrichtung -> Remarketing / ähnliche Zielgruppen / Keywords / Webseiteninhalt / gemeinsame Interessen / Lebensereignisse (Hochschulabschluss, Umzug, Ehe, (alles vorher/nachher). Diese Informationen gerne textlich wie grafisch darstellen
- Information zum Bestellvorgang. Diese Informationen gerne textlich wie grafisch darstellen.
- Kalkulation mit Bestellung (Bestellung führt dann zum erwähnten Layover)
- Portfolio (Vorschau von z.B. 3 Banner plus Aufklappfunktion für weitere Vorschläge)
- Footer
Beispielseite
https://www.flinkwerbung-studio.de/
An der Struktur dieser Webseite würden wir uns gerne anlehnen. Zielmarkt wird jedoch die Deutschschweiz sein.

```html
<!DOCTYPE html>
<html lang="de">
<head>
<meta charset="utf-8">
<title>Bannerwerk Studio – HTML5-Banner zu Festpreisen</title>
<link rel="stylesheet" href="https://fonts.googleapis.com/css2?family=Roboto+Condensed:wght@300;400;700&display=swap">
<style>
:root{
  --blue:#1f6db8;
  --blue-dark:#16589a;
  --blue-text:#1e6ab3;
  --teal:#0d9a93;
  --orange:#ef5a24;
  --orange-dark:#c9431a;
  --green:#8cc63f;
  --grey-bg:#ececec;
  --grey-text:#8a8f96;
  --white:#ffffff;
}
*{margin:0;padding:0;box-sizing:border-box}
html,body{width:1200px;height:2429px;overflow:hidden;background:var(--white)}
body{position:relative;font-family:"Roboto Condensed",Arial,sans-serif;color:var(--grey-text)}
.abs{position:absolute}
.btn{position:absolute;background:linear-gradient(var(--orange),#e04d1c);color:#fff;font-weight:700;text-transform:uppercase;display:flex;align-items:center;justify-content:center;border-radius:2px;box-shadow:0 3px 0 var(--orange-dark)}

/* header */
.site-header{left:0;top:0;width:1200px;height:72px;border-top:3px solid var(--blue);background:#fff}
.brand{left:238px;top:12px;width:300px;height:50px}
.brand-mark{position:absolute;left:0;top:0;width:50px;height:50px;background:var(--blue)}
.brand-name{position:absolute;left:62px;top:6px;font-size:24px;font-weight:700;color:var(--blue-text);line-height:1}
.brand-claim{position:absolute;left:62px;top:36px;font-size:11px;color:var(--blue-text);letter-spacing:.5px;text-transform:uppercase}
.contact{right:248px;top:24px;text-align:right;color:var(--blue-text);line-height:1.1}
.contact small{display:block;font-size:8px;color:var(--grey-text);text-align:left}
.contact .mail{font-size:17px}
.contact .phone{font-size:10px;color:var(--grey-text)}
.contact .phone b{color:var(--blue-text);font-size:12px}

/* hero */
.hero{left:0;top:72px;width:1200px;height:284px;background:linear-gradient(90deg,#1a63ad,#2275c2 60%,#1b68b4);overflow:hidden}
.hero-visual{left:285px;top:58px;width:270px;height:170px;background:linear-gradient(#e9eef3,#8f98a3);border-radius:4px}
.hero-copy{right:289px;top:68px;text-align:right;color:#fff;text-transform:uppercase}
.hero-copy .lead{font-size:17px;font-weight:300;line-height:1.1}
.hero-copy h1{font-size:21px;font-weight:700;line-height:1.1;margin-top:10px}
.hero .btn{right:289px;top:181px;width:172px;height:34px;font-size:18px}
.more-tab{left:525px;top:340px;width:147px;height:33px;background:var(--blue);color:#fff;font-size:12px;font-weight:700;text-align:center;padding-top:6px;z-index:2}
.more-tab svg{display:block;margin:2px auto 0}

/* steps */
.steps{left:0;top:356px;width:1200px;height:485px;background:var(--grey-bg)}
.steps-box{left:288px;top:106px;width:616px;height:330px;background:#fff;border:1px solid #d8d8d8}
.steps-head{right:319px;top:198px;text-align:right;text-transform:uppercase}
.steps-head p{font-size:17px;color:var(--grey-text);font-weight:300}
.steps-head h2{font-size:26px;color:var(--blue-text);line-height:.95;font-weight:700}
.steps-text{left:318px;top:276px;width:563px;font-size:9.5px;line-height:11.3px;text-align:right;text-transform:uppercase;color:#8b8f94;letter-spacing:-.2px}
.steps .btn{left:707px;top:381px;width:172px;height:37px;font-size:18px}

/* consult band */
.consult{left:0;top:841px;width:1200px;height:144px;background:var(--teal);color:#fff;text-align:center;text-transform:uppercase}
.consult p{font-size:27px;font-weight:300;margin-top:38px}
.consult h3{font-size:27px;font-weight:700;margin-top:6px}
.consult h3 span{font-weight:300}

/* calculator */
.calc{left:0;top:985px;width:1200px;height:592px;background:linear-gradient(90deg,#c9cdd0,#e6e4df 40%,#d6d3cc 70%,#b9b7b2)}
.panel{left:256px;width:682px;background:#f2f2f2;border-top:5px solid var(--blue);border-bottom:4px solid var(--blue)}
.benefits{top:33px;height:137px}
.benefits .t1{left:15px;top:16px;font-size:17px;text-transform:uppercase;font-weight:300}
.benefits h2{position:absolute;left:15px;top:33px;font-size:22px;color:var(--blue-text);font-weight:700;text-transform:uppercase}
.benefits ul{position:absolute;left:20px;top:62px;list-style:none;font-size:10px;text-transform:uppercase;line-height:15px}
.benefits li{padding-left:18px;position:relative}
.benefits li svg{position:absolute;left:0;top:2px}
.benefits .aside{position:absolute;right:16px;top:16px;width:280px;font-size:12.5px;line-height:15px;text-align:right;text-transform:uppercase}
.benefits .aside b{color:#5f656c}
.form{top:192px;height:362px;background:#fff;border-bottom:4px solid var(--blue)}
.q{position:absolute;font-size:12.5px;text-transform:uppercase}
.q b{color:var(--blue-text)}
.type-badge{left:91px;top:43px;width:96px;height:96px;border-radius:50%;background:#e4e4e4}
.radio{position:absolute;left:364px;font-size:11.5px;text-transform:uppercase;display:flex;align-items:center;gap:10px}
.radio i{width:20px;height:20px;border-radius:50%;background:#eee;display:inline-block}
.counts{position:absolute;left:27px;top:190px;display:flex;gap:5px}
.counts span{width:38px;height:28px;background:#eef1f4;color:var(--blue-text);font-size:13px;display:flex;align-items:center;justify-content:center}
.counts span.on{background:var(--green);color:#fff;font-weight:700}
.counts span.wide{width:197px}
.price{position:absolute;left:0;top:232px;width:682px;height:126px;background:#f2f2f2}
.price .label{position:absolute;left:18px;top:12px;font-size:27px;font-weight:300;text-transform:uppercase}
.price .vat{position:absolute;left:18px;top:41px;font-size:11px}
.price .sum{position:absolute;right:20px;top:12px;font-size:27px;color:#7a7f86;text-align:right;line-height:1}
.price .sum small{display:block;font-size:11px}
.price .btn{left:442px;top:60px;width:219px;height:37px;font-size:18px}
.price .note{position:absolute;left:18px;top:110px;font-size:8.5px;text-transform:uppercase}

/* clients */
.clients{left:0;top:1577px;width:1200px;height:266px;background:linear-gradient(#1a62ad,#2373c0 50%,#1a62ad);text-align:center}
.clients h2{color:#fff;font-size:27px;font-weight:700;text-transform:uppercase;margin-top:20px}
.ad-tile{top:1651px;width:188px;height:156px;border:1px solid #0d3f72}
</style>
</head>
<body>

<header class="abs site-header">
  <div class="abs brand">
    <span class="brand-mark"></span>
    <span class="brand-name">BANNERWERK STUDIO</span>
    <span class="brand-claim">HTML5-Werbung nach Mass</span>
  </div>
  <div class="abs contact">
    <small>Schreiben Sie uns:</small>
    <div class="mail">INFO@BANNERWERK-STUDIO.CH</div>
    <div class="phone">ODER RUFEN SIE UNS AN: <b>044 555 01 23</b></div>
  </div>
</header>

<section class="abs hero">
  <svg class="abs" style="left:0;top:0" width="1200" height="284" aria-hidden="true">
    <polygon points="40,284 220,110 400,284" fill="#ffffff" opacity=".12"/>
    <polygon points="150,284 240,200 330,284" fill="#ffffff" opacity=".18"/>
    <polygon points="760,0 900,140 1040,0" fill="#ffffff" opacity=".14"/>
    <polygon points="880,0 950,60 1020,0" fill="#ffffff" opacity=".4"/>
    <polygon points="1060,0 1200,140 1200,0" fill="#ffffff" opacity=".1"/>
  </svg>
  <div class="abs hero-visual" role="img" aria-label="Laptop mit Bannerentwurf auf dem Bildschirm"></div>
  <div class="abs hero-copy">
    <p class="lead">Sie suchen den richtigen Partner<br>für Ihre nächste Online-Kampagne?</p>
    <h1>Wir sind Ihre Experten für<br>professionelle HTML5-Banner!</h1>
  </div>
  <div class="btn">Jetzt kalkulieren</div>
</section>
<div class="abs more-tab">MEHR ERFAHREN<svg width="22" height="7" aria-hidden="true"><path d="M1 1l5 5 5-5M11 1l5 5 5-5" fill="none" stroke="#fff" stroke-width="1"/></svg></div>

<section class="abs steps">
  <div class="abs steps-box"></div>
  <svg class="abs" style="left:0;top:0" width="1200" height="485" aria-hidden="true">
    <g fill="none" stroke="#d0d0d0" stroke-width="1.5">
      <polyline points="288,240 288,232 350,232 411,232 411,208 473,208 534,208 534,170 600,170 660,170 660,140 720,140 780,140 780,109 841,109 904,109"/>
    </g>
    <g fill="#fff" stroke="#d6d6d6" stroke-width="1.5">
      <circle cx="350" cy="226" r="40"/><circle cx="473" cy="192" r="40"/>
      <circle cx="600" cy="155" r="40"/><circle cx="720" cy="124" r="40"/>
      <circle cx="841" cy="94" r="40"/>
    </g>
    <g fill="none" stroke="#8cc63f" stroke-width="3" stroke-linecap="round">
      <path d="M283 240l6 6 11-12"/><path d="M406 206l6 6 11-12"/><path d="M529 172l6 6 11-12"/>
      <path d="M652 138l6 6 11-12"/><path d="M775 106l6 6 11-12"/>
    </g>
    <g font-family="Roboto Condensed, sans-serif" text-anchor="middle">
      <g fill="#1e6ab3" font-size="34" font-weight="300">
        <text x="350" y="231">1</text><text x="473" y="197">2</text><text x="600" y="160">3</text>
        <text x="720" y="129">4</text><text x="841" y="99">5</text>
      </g>
      <g fill="#8a8f96" font-size="9.5">
        <text x="350" y="242">BERATUNG</text><text x="473" y="208">VORSCHLAG</text><text x="600" y="171">FEEDBACK</text>
        <text x="720" y="140">UMSETZUNG</text><text x="841" y="110">AUSLIEFERUNG</text>
      </g>
    </g>
  </svg>
  <div class="abs steps-head">
    <p>Und so einfach geht´s</p>
    <h2>In fünf Schritten zum<br>fertigen HTML5-Banner</h2>
  </div>
  <p class="abs steps-text">Im persönlichen Gespräch definieren wir gemeinsam Ihre Ziele. An welche Zielgruppe möchten Sie welches<br>Produkt vermarkten? Wie ist Ihr Zeitplan und wie Ihr Budget? Gemeinsam planen wir die Bannerkampagne<br>nach Ihren Wünschen. Nach unserem Gespräch erstellen wir Ihnen ein Angebot mit verlässlichen Festpreisen.<br>Jetzt geht es ins Detail! Wir entwickeln kreative Ideen, um Ihre Inhalte umzusetzen.<br>Dabei behalten wir immer Ihren Zeitplan und Ihr Budget im Auge. Wir finden die optimale Lösung<br>für Ihr Produkt. Mit aktuellster Technik programmieren wir Ihre Werbebanner sorgfältig und individuell.<br>Natürlich erfüllen unsere animierten HTML5-Banner alle Anforderungen Ihres Werbenetzwerkes.<br>Auf Wunsch übermitteln wir die Daten auch direkt an Ihren Medienpartner oder Publisher.</p>
  <div class="btn">Jetzt kalkulieren</div>
</section>

<section class="abs consult">
  <p>Wir beraten Sie gerne:</p>
  <h3>044 555 01 23 <span>oder</span> per E-Mail</h3>
</section>

<section class="abs calc" role="img" aria-label="Foto eines Teams bei der Arbeit im Büro">
  <div class="abs panel benefits">
    <p class="abs t1">HTML5-Banner zu Festpreisen</p>
    <h2>Ihre Vorteile auf einen Blick</h2>
    <ul>
      <li><svg width="12" height="10"><path d="M1 5l3 3 7-7" fill="none" stroke="#1e6ab3" stroke-width="2"/></svg>Persönliche Beratung</li>
      <li><svg width="12" height="10"><path d="M1 5l3 3 7-7" fill="none" stroke="#1e6ab3" stroke-width="2"/></svg>Entwicklung nach Vorgaben Ihrer Werbenetzwerke</li>
      <li><svg width="12" height="10"><path d="M1 5l3 3 7-7" fill="none" stroke="#1e6ab3" stroke-width="2"/></svg>Auf Wunsch direkte Lieferung an Ihre Mediaagentur</li>
      <li>oder Publisher wie Velmora Display, Klickwerk, Rollkanal, Formad usw.</li>
    </ul>
    <p class="aside"><b>Mit unseren Festpreisen bleiben<br>Sie immer im Budget</b>. Die folgenden<br>Preise sind für Standardformate.<br>Natürlich machen wir Ihnen<br>auch gerne ein persönliches<br>Angebot für Sonderformate,<br>Interaktion und Rich Media.</p>
  </div>

  <div class="abs panel form">
    <p class="q" style="left:19px;top:20px"><b>1.</b> Welche Art Banner benötigen Sie?</p>
    <div class="abs type-badge"></div>
    <svg class="abs" style="left:150px;top:80px" width="60" height="48" aria-hidden="true"><path d="M6 22l16 18 32-34" fill="none" stroke="#8cc63f" stroke-width="8" stroke-linecap="round"/></svg>
    <p class="q" style="left:351px;top:20px"><b>2.</b> Gibt es eine Designvorlage?</p>
    <div class="radio" style="top:46px"><svg width="20" height="16"><path d="M2 8l6 6 10-12" fill="none" stroke="#8cc63f" stroke-width="3"/></svg>Designvorlagen vorhanden</div>
    <div class="radio" style="top:74px"><i></i><span><b>Keine</b> Designvorlage vorhanden</span></div>
    <p class="q" style="left:19px;top:160px"><b>3.</b> Wieviele Banner benötigen Sie?</p>
    <div class="counts">
      <span>01</span><span>02</span><span class="on">03</span><span>04</span><span>05</span><span>06</span><span>08</span><span>10</span><span>12</span><span>16</span><span class="wide">ANDERE ANZAHL BANNER</span>
    </div>
    <div class="price">
      <p class="label">Kampagnenpreis*:</p>
      <p class="vat">ZZGL. 7,7% MWST.</p>
      <p class="sum">1000,00 €<small>77,00 €</small></p>
      <div class="btn">Angebot anfragen</div>
      <p class="note">* Es handelt sich hier um erste Richtpreise. Fragen Sie einfach unverbindlich an, dann machen wir Ihnen ein konkretes Angebot!</p>
    </div>
  </div>
</section>

<section class="abs clients">
  <h2>Kunden die unser Angebot nutzen:</h2>
  <svg class="abs" style="left:46px;top:95px" width="30" height="46" aria-hidden="true"><path d="M24 4L6 23l18 19" fill="none" stroke="#fff" stroke-width="5"/></svg>
  <svg class="abs" style="left:1126px;top:95px" width="30" height="46" aria-hidden="true"><path d="M6 4l18 19L6 42" fill="none" stroke="#fff" stroke-width="5"/></svg>
</section>
<div class="abs ad-tile" style="left:96px;background:linear-gradient(#1b4a8a,#5a6c80)" role="img" aria-label="Kundenbanner für Tischtennistische"></div>
<div class="abs ad-tile" style="left:302px;background:linear-gradient(#c9d6e4,#1c4f8c)" role="img" aria-label="Kundenbanner eines Immobilienmaklers"></div>
<div class="abs ad-tile" style="left:506px;background:linear-gradient(#3a1414,#1a1a1a)" role="img" aria-label="Kundenbanner für Haarpflegeprodukte"></div>
<div class="abs ad-tile" style="left:712px;background:linear-gradient(#ffffff,#dcdcdc)" role="img" aria-label="Kundenbanner eines Autohändlers"></div>
<div class="abs ad-tile" style="left:917px;background:linear-gradient(#8a5a2b,#2a1a0e)" role="img" aria-label="Kundenbanner für einen Holzbau-Kurs"></div>

</body>
</html>
```